Business card design needed

My business is in Matchmaking. My objective is to find the most compatible partner for my clients....basically I'm in the love and happiness industry bringing two people together for a lasting loving relationship.

I envision the design to be something with 2 people who are in love looking happy or even a silhouette.....I don't really know, I'm open to ideas.....maybe no picture at all, but I want it to be classy :-)

I do have a logo which I will upload. You can also go to my website to give you an idea on the colours and the design if that helps, however the website is not finished yet, it should be up by today or tomorrow. If the website has a heart with swirls on the upper left hand corner, that is the old website, please ignore that one. The one that will be up shortly has a picture frame on the home page with my logo that will be in the file I will upload on this page.

Target Market(s)

There are three categories: Over 45, Asian and Western and same sex, but would be able to afford to hire a matchmaker

Industry/Entity Type

Industry

Contact Information for Business Card

The Tidewell Bureau
Helping You Find The "One"
Maris Pelloway
Matchmaker
0491 572 064
info@tidewellbureau.com.au
www.tidewellbureau.com.au

```html
<!DOCTYPE html>
<html lang="en">
<head>
<meta charset="utf-8">
<title>The Tidewell Bureau – Business Card</title>
<link rel="stylesheet" href="https://fonts.googleapis.com/css2?family=Roboto:ital,wght@0,400;0,700;1,400&display=swap">
<style>
  :root {
    --page: #ffffff;
    --teal: #7ab3a5;
    --ink-light: #ffffff;
    --ink-dark: #4e5b61;
  }
  * { margin: 0; padding: 0; box-sizing: border-box; }
  html, body {
    width: 1200px;
    height: 738px;
    overflow: hidden;
    background: var(--page);
    font-family: "Roboto", "Helvetica Neue", Arial, sans-serif;
  }
  .canvas {
    position: relative;
    width: 1200px;
    height: 738px;
  }
  .card {
    position: absolute;
    left: 406px;
    top: 23px;
    width: 398px;
    height: 684px;
    display: flex;
    flex-direction: column;
  }
  .card__brand {
    height: 245px;
    border: 1.5px solid var(--teal);
    border-bottom: none;
    display: flex;
    align-items: center;
    justify-content: center;
    gap: 12px;
  }
  .brand-dot {
    width: 14px;
    height: 14px;
    border-radius: 50%;
    background: var(--ink-dark);
  }
  .brand-name {
    color: var(--ink-dark);
    font-size: 30px;
    font-weight: 400;
    letter-spacing: 0.3px;
  }
  .card__details {
    flex: 1;
    background: var(--teal);
    color: var(--ink-light);
    text-align: center;
    padding-top: 60px;
  }
  .contact-group { line-height: 31px; }
  .contact-group + .contact-group { margin-top: 52px; }
  .strong { font-weight: 700; font-size: 23px; }
  .soft { font-style: italic; font-size: 22px; font-weight: 400; }
</style>
</head>
<body>
<main class="canvas">
  <article class="card">
    <header class="card__brand">
      <span class="brand-dot"></span>
      <span class="brand-name">The Tidewell Bureau</span>
    </header>
    <section class="card__details">
      <div class="contact-group">
        <p class="strong">Maris Pelloway</p>
        <p class="soft">Matchmaker</p>
      </div>
      <div class="contact-group">
        <p class="strong">Ph: 0491 572 064</p>
        <p class="soft">info@tidewellbureau.com.au</p>
      </div>
      <div class="contact-group">
        <p class="strong">www.tidewellbureau.com.au</p>
        <p class="soft">Helping You Find The “One”</p>
      </div>
    </section>
  </article>
</main>
</body>
</html>
```